Redesign of an existing webpage

We've just redesigned our logo on a new website design to reflect the new logo. That wants to change the color and graphical appearance of our website. There are no restrictions on what should be changed. IT should display our portfolio and pricing and explain our product. Please provide stock photos if needed. The site structure should not be changed. So we want the pages which are currently there. We need the following pages: Main page (Home page) Detail page (currently used at AGB and questions) Imprint (including the map) existing webpage: www.brightdune.de
Updates

I've got a request from one of the designers-

Target Market(s)

We are offering IT services to small companies. The do not need own IT equipment or PC Specialists if if our service.

Industry/Entity Type

It Service

Coding

Coded - Design and coding required

Number of Pages Required

3 page

Font styles to use
Other font styles liked:
• Relaway

Colors

Designer to choose colors to be used in the design.

Requirements
Must have
• our login mask at https://desktop.brightdune.com needs a rebranding too

```html
<!DOCTYPE html>
<html lang="en">
<head>
<meta charset="utf-8">
<title>BrightDune – Menu</title>
<link rel="stylesheet" href="https://fonts.googleapis.com/css2?family=Raleway:wght@500;600;700;800&family=Oswald:wght@400&display=swap">
<style>
  :root {
    --bg: #0c0c0d;
    --text-muted: #8e8e94;
    --text-light: #ffffff;
    --accent: #1c6fbf;
    --accent-soft: #4a84c4;
    --rule: #5a5a60;
  }
  * { margin: 0; padding: 0; box-sizing: border-box; }
  html, body {
    width: 1200px; height: 600px; overflow: hidden;
    background: var(--bg);
    font-family: "Raleway", sans-serif;
  }
  .menu-screen {
    position: relative; width: 1200px; height: 600px;
    background: radial-gradient(ellipse at 40% 40%, #141416 0%, var(--bg) 70%);
  }
  .brand {
    position: absolute; left: 80px; top: 30px;
    display: flex; align-items: center; gap: 10px;
    font-weight: 800; font-size: 28px; letter-spacing: 1px;
    color: var(--text-light);
  }
  .brand-dot {
    width: 14px; height: 14px; border-radius: 50%;
    background: var(--accent);
  }
  .login-link {
    position: absolute; left: 816px; top: 41px;
    font-size: 11px; font-weight: 700; letter-spacing: 1px;
    color: var(--text-light); text-decoration: none;
  }
  .cta-button {
    position: absolute; left: 893px; top: 32px;
    width: 152px; height: 32px; border-radius: 16px;
    background: var(--accent-soft); color: var(--text-light);
    font-size: 10px; font-weight: 700; letter-spacing: 0.8px;
    display: flex; align-items: center; justify-content: center;
    text-decoration: none;
  }
  .close-icon { position: absolute; left: 1103px; top: 41px; }
  .nav-column {
    position: absolute; top: 172px; list-style: none;
  }
  .nav-column li {
    height: 28.8px; line-height: 24px;
    font-size: 17px; font-weight: 600; color: var(--text-muted);
    letter-spacing: 0.3px;
  }
  .nav-column.primary { left: 156px; }
  .nav-column.legal { left: 460px; }
  .nav-column li.is-active {
    color: var(--accent); position: relative; padding-left: 14px;
  }
  .nav-column li.is-active::before {
    content: ""; position: absolute; left: -24px; top: 12px;
    width: 24px; height: 1px; background: var(--rule);
  }
  .support {
    position: absolute; left: 763px; top: 170px;
  }
  .support-title {
    font-size: 17px; font-weight: 700; color: var(--accent);
    letter-spacing: 0.3px;
  }
  .support-email {
    margin-top: 22px; font-size: 15.5px; font-weight: 600;
    color: var(--text-muted);
  }
  .support-phone {
    margin-top: 8px; font-family: "Oswald", sans-serif;
    font-size: 15px; color: var(--text-muted); letter-spacing: 0.3px;
  }
  .contact-button {
    position: absolute; left: 2px; top: 120px;
    width: 128px; height: 40px; border-radius: 20px;
    border: 1px solid var(--accent); color: var(--accent);
    font-size: 10px; font-weight: 700; letter-spacing: 1px;
    display: flex; align-items: center; justify-content: center;
  }
  .copyright {
    position: absolute; left: 156px; top: 510px;
    font-size: 10px; font-weight: 600; letter-spacing: 1px;
    color: var(--text-muted);
  }
  .copyright strong { color: var(--text-light); font-weight: 700; }
  .social-links {
    position: absolute; left: 764px; top: 501px;
    display: flex; gap: 8px;
  }
  .social-links span {
    width: 32px; height: 32px; border-radius: 50%;
    border: 1px solid var(--accent-soft);
  }
  .social-links span.is-active { background: var(--accent-soft); }
</style>
</head>
<body>
<main class="menu-screen">
  <div class="brand"><span class="brand-dot"></span>BRIGHTDUNE</div>
  <a class="login-link" href="#">LOG IN</a>
  <a class="cta-button" href="#">GET STARTED NOW!</a>
  <svg class="close-icon" width="14" height="14" viewBox="0 0 14 14" aria-label="Close menu">
    <path d="M1 1L13 13M13 1L1 13" stroke="#ffffff" stroke-width="2" stroke-linecap="round"/>
  </svg>

  <ul class="nav-column primary">
    <li>Home</li>
    <li class="is-active">That's How It's Done</li>
    <li>Prices</li>
    <li>About Us</li>
    <li>Ask</li>
  </ul>

  <ul class="nav-column legal">
    <li>Data Protection</li>
    <li>Conditions</li>
    <li>Imprint</li>
  </ul>

  <section class="support">
    <h2 class="support-title">Help &amp; Support</h2>
    <p class="support-email">E. kunde@brightdune.de</p>
    <p class="support-phone">+49 2924 5510372</p>
    <a class="contact-button">CONTACT US</a>
  </section>

  <p class="copyright">© 2019 <strong>BRIGHTDUNE</strong>. ALL RIGTH RESERVED.</p>

  <nav class="social-links" aria-label="Social links">
    <span></span><span class="is-active"></span><span></span><span></span>
  </nav>
</main>
</body>
</html>
```